We need a nice stationary and business card design for our new mobile ultrasound company.
Kestral Sonics, LLC
We need a nice stationary and business card design for our new mobile ultrasound company.  - Medical
Creative Brief
Bright & Fun-filled
Tomaso Fairbank
Vice President
5817 E. Halvering Ct
Tomaso.Fairbank@kestralsonics.example
KestralSonics.example
Please do not add our address to your design.

```html
<!DOCTYPE html>
<html lang="en">
<head>
<meta charset="utf-8">
<title>Kestral Sonics — Business Card</title>
<link href="https://fonts.googleapis.com/css2?family=Arimo:wght@400;700&display=swap" rel="stylesheet">
<style>
  :root {
    --bg: #e6e7e9;
    --card: #ffffff;
    --blue: #1f7fc6;
    --blue-deep: #0d5fa6;
    --blue-light: #4aa3e0;
    --blue-soft: #7fb8e4;
    --grey: #7d8287;
    --grey-line: #a9adb2;
    --white: #ffffff;
  }
  * { margin: 0; padding: 0; box-sizing: border-box; }
  html, body {
    width: 1200px; height: 838px; overflow: hidden;
    background: var(--bg);
    font-family: "Arimo", Arial, sans-serif;
  }
  .card {
    position: absolute;
    width: 880px; height: 500px;
    box-shadow: 0 18px 40px rgba(0,0,0,0.2);
    overflow: hidden;
  }

  /* Back side */
  .card-back {
    left: 280px; top: 40px;
    background: linear-gradient(135deg, var(--blue-light) 0%, var(--blue) 50%, var(--blue-deep) 100%);
  }
  .back-pattern {
    position: absolute; left: 120px; top: 20px;
    width: 720px; height: 230px;
    background: radial-gradient(ellipse at 50% 45%, rgba(127,184,228,0.55) 0%, rgba(127,184,228,0.25) 45%, rgba(127,184,228,0) 72%);
  }

  /* Front side */
  .card-front {
    left: 40px; top: 300px;
    background: var(--card);
  }
  .card-wave { position: absolute; left: 0; top: 0; width: 880px; height: 500px; }
  .brand {
    position: absolute; left: 80px; top: 70px;
    display: flex; align-items: center; gap: 22px;
  }
  .brand-mark {
    width: 82px; height: 82px; border-radius: 50%;
    background: var(--blue);
  }
  .brand-name {
    font-weight: 700; color: var(--blue);
    font-size: 50px; line-height: 1; letter-spacing: 1px;
    text-transform: uppercase;
  }
  .person { position: absolute; left: 80px; top: 196px; }
  .person-name {
    font-weight: 700; font-size: 26px; text-transform: uppercase;
    letter-spacing: 0.5px;
  }
  .person-name .first { color: var(--blue); }
  .person-name .last { color: var(--grey); }
  .person-title { font-size: 15px; color: var(--grey); margin-top: 4px; }
  .contact {
    position: absolute; right: 44px; top: 360px;
    color: var(--white); font-size: 17px; line-height: 1.5;
    text-align: right; list-style: none;
  }
  .contact li { display: flex; justify-content: flex-end; align-items: center; gap: 9px; }
  .contact svg { width: 16px; height: 16px; fill: var(--white); }
  .contact .email { margin-bottom: 10px; }
</style>
</head>
<body>
  <div class="card card-back">
    <div class="back-pattern" role="img" aria-label="Soft circular bubble pattern in light blue"></div>
  </div>

  <div class="card card-front">
    <svg class="card-wave" viewBox="0 0 880 500" aria-hidden="true">
      <defs>
        <linearGradient id="waveFill" x1="0" y1="0" x2="1" y2="1">
          <stop offset="0" stop-color="var(--blue-light)"/>
          <stop offset="0.55" stop-color="var(--blue)"/>
          <stop offset="1" stop-color="var(--blue-deep)"/>
        </linearGradient>
      </defs>
      <path d="M0 315 C 195 332, 335 410, 495 367 C 635 328, 755 262, 880 288 L880 500 L0 500 Z" fill="url(#waveFill)"/>
      <path d="M0 302 C 195 317, 335 393, 495 351 C 635 313, 755 247, 880 272" fill="none" stroke="var(--grey-line)" stroke-width="4"/>
      <path d="M0 333 C 210 350, 352 428, 510 385 C 650 346, 765 284, 880 306" fill="none" stroke="var(--white)" stroke-width="2.5" opacity="0.6"/>
    </svg>

    <div class="brand">
      <span class="brand-mark"></span>
      <span class="brand-name">Kestral Sonics</span>
    </div>

    <div class="person">
      <p class="person-name"><span class="first">Tomaso</span> <span class="last">Fairbank</span></p>
      <p class="person-title">Vice President</p>
    </div>

    <ul class="contact">
      <li class="email">
        <svg viewBox="0 0 24 24"><path d="M2 5h20v14H2z M3 6l9 7 9-7" fill="none" stroke="#fff" stroke-width="2"/></svg>
        Tomaso.Fairbank@kestralsonics.example
      </li>
      <li>
        <svg viewBox="0 0 24 24"><path d="M6.6 10.8c1.4 2.8 3.8 5.1 6.6 6.6l2.2-2.2c.3-.3.7-.4 1-.2 1.1.4 2.3.6 3.6.6.6 0 1 .4 1 1V20c0 .6-.4 1-1 1C10.6 21 3 13.4 3 4c0-.6.4-1 1-1h3.5c.6 0 1 .4 1 1 0 1.3.2 2.5.6 3.6.1.3 0 .7-.2 1z"/></svg>
        (555) 310-2740
      </li>
      <li>
        <svg viewBox="0 0 24 24"><path d="M6 3h10v5H6z M3 9h18v9h-3v3H6v-3H3z M8 15v4h8v-4z"/></svg>
        (555) 310-2741
      </li>
      <li>www.KestralSonics.example</li>
    </ul>
  </div>
</body>
</html>
```